Belvoro Website

I need a website for a startup company that provides GIS (Geographic Information Services) staffing and products for local cities. Current website is www.belvorogroup.com

```html
<!DOCTYPE html>
<html lang="en">
<head>
<meta charset="utf-8">
<title>Belvoro Group — We Make GIS Work For You</title>
<link href="https://fonts.googleapis.com/css2?family=Outfit:wght@400;500;600;700&display=swap" rel="stylesheet">
<style>
  :root {
    --ink: #111214;
    --dark: #151515;
    --card: #2b2b2c;
    --blue: #1a74b8;
    --blue-bright: #1f8fe0;
    --white: #ffffff;
    --text: #2a2a2a;
    --rule: #3a3a3a;
    --hero-base: #121316;
    --hero-tint: #10243c;
  }
  * { box-sizing: border-box; margin: 0; padding: 0; }
  html, body { width: 1200px; height: 2242px; overflow: hidden; }
  body { position: relative; background: var(--white); font-family: "Outfit", sans-serif; color: var(--text); }

  .brand { position: absolute; display: flex; align-items: center; gap: 10px; color: var(--white); font-weight: 700; letter-spacing: -0.3px; }
  .brand-dot { border-radius: 50%; background: var(--blue); }
  .nav { position: absolute; display: flex; gap: 33px; font-size: 12px; color: var(--white); text-transform: uppercase; }

  /* Hero */
  .hero { position: absolute; left: 0; top: 0; width: 1200px; height: 675px; background: var(--hero-base); border-bottom: 7px solid #0c1a2a; overflow: hidden; }
  .hero-backdrop { position: absolute; inset: 0; background: linear-gradient(160deg, var(--hero-base) 0%, var(--hero-base) 35%, var(--hero-tint) 75%, #0e1a28 100%); }
  .site-header { position: absolute; left: 94px; top: 0; width: 1012px; height: 65px; border-bottom: 1px solid #2c2c2c; }
  .site-header .brand { left: 0; top: 14px; font-size: 25px; }
  .site-header .brand-dot { width: 28px; height: 28px; }
  .site-header .nav { right: 0; top: 25px; }
  .hero-title { position: absolute; left: 0; width: 1200px; top: 283px; text-align: center; font-size: 55px; font-weight: 700; color: var(--white); letter-spacing: -0.5px; line-height: 66px; }
  .hero-sub { position: absolute; left: 0; width: 1200px; top: 355px; text-align: center; font-size: 26px; font-weight: 600; color: var(--white); line-height: 32px; }
  .scroll-cue { position: absolute; left: 591px; top: 610px; }

  /* Company */
  .photo { position: absolute; border-radius: 12px; }
  .sliver { left: -10px; top: 773px; width: 25px; height: 321px; background: linear-gradient(180deg, #2a2520, #c07a30 60%, #1c1a18); }
  .map-photo { left: 26px; top: 773px; width: 206px; height: 321px; background: linear-gradient(160deg, #2f7fd0 0%, #1a1d1c 30%, #2c4a22 70%, #151a14); }
  .city-photo { left: 240px; top: 773px; width: 396px; height: 321px; background: linear-gradient(180deg, #d8c9b4 0%, #8d8a83 35%, #3f5a38 60%, #3a3a3a 100%); }
  .slide-dots { position: absolute; left: 404px; top: 1054px; display: flex; gap: 6px; }
  .slide-dots span { width: 20px; height: 2px; background: var(--white); }
  .slide-dots span:first-child { background: var(--blue); }
  .company-title { position: absolute; left: 712px; top: 876px; font-size: 40px; font-weight: 700; color: var(--ink); letter-spacing: -0.3px; line-height: 48px; }
  .company-text { position: absolute; left: 713px; top: 932px; width: 342px; font-size: 13.5px; line-height: 19px; color: var(--text); }

  /* Services */
  .services { position: absolute; left: 94px; top: 1189px; width: 1012px; height: 449px; border-radius: 43px; background: linear-gradient(135deg, #1d1d1f, #141415 60%, #1a1a1b); }
  .services-kicker { position: absolute; left: 0; width: 1200px; top: 1259px; text-align: center; font-size: 19px; font-weight: 700; color: var(--blue); line-height: 24px; }
  .services-title { position: absolute; left: 0; width: 1200px; top: 1285px; text-align: center; font-size: 38px; font-weight: 700; color: var(--white); letter-spacing: -0.3px; line-height: 46px; }
  .service-card { position: absolute; top: 1343px; width: 269px; height: 351px; border-radius: 12px; background: var(--card); padding: 3px; }
  .service-card.featured { background: var(--blue); }
  .service-card .thumb { width: 263px; height: 179px; border-radius: 10px; }
  .service-card h3 { margin: 14px 0 0 24px; font-size: 20px; font-weight: 700; color: var(--white); }
  .service-card ul { list-style: none; margin: 10px 0 0 24px; }
  .service-card li { font-size: 12.5px; line-height: 16.6px; color: var(--white); padding-left: 13px; position: relative; }
  .service-card li::before { content: "›"; position: absolute; left: 0; top: -1px; color: #9a9a9a; }
  .service-card.featured li::before { color: #cde3f5; }
  .consulting { left: 185px; }
  .applications { left: 467px; }
  .spatial { left: 749px; }
  .thumb-consulting { background: linear-gradient(135deg, #1b2f6a, #3a5fb8 45%, #c9a87a 85%); }
  .thumb-apps { background: linear-gradient(160deg, #9fd2ea, #2f6e90 50%, #1b2a33); }
  .thumb-spatial { background: linear-gradient(135deg, #2a2f5c, #1a1c24 50%, #2d3170); }

  /* CTA */
  .cta-title { position: absolute; left: 0; width: 1200px; top: 1785px; text-align: center; font-size: 38px; font-weight: 700; color: var(--ink); letter-spacing: -0.3px; line-height: 46px; }
  .cta-text { position: absolute; left: 0; width: 1200px; top: 1840px; text-align: center; font-size: 14px; color: var(--text); }
  .cta-button { position: absolute; left: 524px; top: 1876px; width: 152px; height: 44px; border-radius: 22px; background: var(--blue); color: var(--white); font-size: 14px; font-weight: 500; display: flex; align-items: center; justify-content: center; }

  /* Footer */
  .site-footer { position: absolute; left: 0; top: 2000px; width: 1200px; height: 242px; border-radius: 43px 43px 0 0; background: var(--dark); }
  .site-footer .brand { left: 94px; top: 82px; font-size: 40px; }
  .site-footer .brand-dot { width: 44px; height: 44px; }
  .footer-address { position: absolute; right: 97px; top: 82px; display: flex; align-items: center; gap: 8px; font-size: 13px; color: var(--white); }
  .site-footer .nav { right: 94px; top: 112px; }
  .footer-rule { position: absolute; left: 94px; top: 191px; width: 1012px; height: 1px; background: var(--rule); }
  .copyright { position: absolute; left: 0; width: 1200px; top: 210px; text-align: center; font-size: 13px; color: var(--white); }
  .to-top { position: absolute; left: 1129px; top: 172px; width: 34px; height: 34px; border-radius: 50%; background: var(--blue); display: flex; align-items: center; justify-content: center; }
</style>
</head>
<body>

<section class="hero">
  <div class="hero-backdrop" role="img" aria-label="Night view of Earth from orbit with city lights and a blue atmosphere"></div>
  <header class="site-header">
    <div class="brand"><span class="brand-dot"></span>Belvoro</div>
    <nav class="nav"><span>About</span><span>Services</span><span>Contact</span></nav>
  </header>
  <h1 class="hero-title">Belvoro Group</h1>
  <p class="hero-sub">We Make GIS Work For You</p>
  <svg class="scroll-cue" width="18" height="28" viewBox="0 0 18 28" aria-hidden="true">
    <rect x="1" y="1" width="16" height="26" rx="8" fill="none" stroke="#fff" stroke-width="1.6"/>
    <line x1="9" y1="7" x2="9" y2="13" stroke="#fff" stroke-width="1.6" stroke-linecap="round"/>
  </svg>
</section>

<section class="company">
  <div class="photo sliver" role="img" aria-label="City lights at dusk"></div>
  <div class="photo map-photo" role="img" aria-label="Dark street map of a city with green parks and a blue river"></div>
  <div class="photo city-photo" role="img" aria-label="Aerial city skyline above a park with a red location pin inside a focus frame"></div>
  <div class="slide-dots"><span></span><span></span><span></span></div>
  <h2 class="company-title">Our Company</h2>
  <p class="company-text">We are an innovative team of geospatial experts with 25 years of experience in the field of GIS. We specialize in providing results-driven GIS solutions for local government and the private sector.</p>
</section>

<section class="services-section">
  <div class="services" role="img" aria-label="Dark street map background"></div>
  <p class="services-kicker">Our services</p>
  <h2 class="services-title">We make GIS work for you</h2>

  <article class="service-card consulting">
    <div class="thumb thumb-consulting" role="img" aria-label="GIS analysts working at monitors showing maps"></div>
    <h3>GIS Consulting</h3>
    <ul>
      <li>GIS projects</li><li>Staffing solutions</li><li>System architecture design</li>
      <li>GIS analysis</li><li>Demographics</li><li>Map products</li>
    </ul>
  </article>

  <article class="service-card applications featured">
    <div class="thumb thumb-apps" role="img" aria-label="Hands using a tablet displaying a map application"></div>
    <h3>GIS Applications</h3>
    <ul>
      <li>AtlasCloud Online</li><li>AtlasCloud Enterprise</li><li>Dashboards</li>
      <li>Experience Studio</li><li>Custom widgets</li><li>Custom JavaScript apps</li>
    </ul>
  </article>

  <article class="service-card spatial">
    <div class="thumb thumb-spatial" role="img" aria-label="Abstract network of glowing blue data lines"></div>
    <h3>Spatial Data Solutions</h3>
    <ul>
      <li>Spatial data cleanup</li><li>GIS data model design/review</li><li>Integrating with other systems</li>
    </ul>
  </article>
</section>

<section class="cta">
  <h2 class="cta-title">Let's Partner on your next project</h2>
  <p class="cta-text">There is no project too big or small. We look forward to hearing from you</p>
  <a class="cta-button">Contact Us</a>
</section>

<footer class="site-footer">
  <div class="brand"><span class="brand-dot"></span>Belvoro</div>
  <p class="footer-address">
    <svg width="9" height="12" viewBox="0 0 9 12" aria-hidden="true"><path d="M4.5 0C2 0 0 2 0 4.4 0 7.6 4.5 12 4.5 12S9 7.6 9 4.4C9 2 7 0 4.5 0Z" fill="#1f8fe0"/><circle cx="4.5" cy="4.4" r="1.6" fill="#151515"/></svg>
    480 N. Larkspur Ave. #210 Oakridge, CA 90412
  </p>
  <nav class="nav"><span>About</span><span>Services</span><span>Contact</span></nav>
  <div class="footer-rule"></div>
  <p class="copyright">©Copyright 2024 Belvoro Group | All Rights Reserved</p>
  <a class="to-top" aria-label="Back to top">
    <svg width="10" height="7" viewBox="0 0 10 7" aria-hidden="true"><path d="M1 6l4-4 4 4" fill="none" stroke="#fff" stroke-width="1.6"/></svg>
  </a>
</footer>

</body>
</html>
```